Business Card Design

We need a business card design for a new company based in Melbourne Australia. We are financial broker in finance industry. We provide a wide range of finance solutions to our clients including home loans, commercial loans, business facilities, car loans, equipment loans, invoice finance, etc. The company name is from director's personal name. We would like to have a new company logo that includes TK.

Industry/Entity Type

Business

Contact Information for Business Card

company name: TK & Co Finance Pty Ltd
person's name: Desmond Okafor
role: Managing Director
Mobile: 0417 638 294
fax: 03 9561 4472
Email: desmond.okafor@tkcolending.example
Address: Suite 5/418 Marlow Avenue Elmvale Vic 3174
Credit Licence No.: 718249

```html
<!DOCTYPE html>
<html lang="en">
<head>
<meta charset="utf-8">
<title>TK &amp; Co Finance Pty Ltd – Business Card</title>
<link href="https://fonts.googleapis.com/css2?family=Ubuntu:wght@400;500;700&display=swap" rel="stylesheet">
<style>
  :root {
    --navy: #1f3a82;
    --navy-deep: #182f6c;
    --gold: #f0a21e;
    --white: #ffffff;
    --paper: #f4f4f4;
    --stage: #e6e6e3;
    --text-font: "Ubuntu", Arial, sans-serif;
  }
  * { box-sizing: border-box; margin: 0; padding: 0; }
  html, body { width: 1200px; height: 780px; overflow: hidden; }
  body {
    background: var(--stage);
    font-family: var(--text-font);
    position: relative;
  }
  .card {
    position: absolute;
    top: 231px;
    width: 520px;
    height: 318px;
    overflow: hidden;
    box-shadow: 0 6px 18px rgba(0,0,0,.18);
  }
  /* Front */
  .card-front { left: 50px; background: var(--paper); }
  .card-front .shape { position: absolute; inset: 0; }
  .front-brand {
    position: absolute;
    left: 36px;
    top: 96px;
    color: var(--navy);
  }
  .brand-mark {
    display: flex;
    align-items: center;
    gap: 10px;
    font-weight: 700;
    font-size: 74px;
    line-height: 1;
    letter-spacing: -2px;
  }
  .brand-dot {
    width: 15px; height: 15px; border-radius: 50%;
    background: var(--gold);
  }
  .company-name {
    font-size: 17px;
    font-weight: 400;
    margin-top: 10px;
    white-space: nowrap;
  }
  .licence {
    font-size: 12px;
    margin-top: 6px;
    padding-left: 30px;
  }
  .contact {
    position: absolute;
    right: 20px;
    top: 36px;
    text-align: right;
    color: var(--white);
  }
  .person-name {
    font-weight: 700;
    font-size: 18px;
    text-transform: uppercase;
    letter-spacing: .3px;
    white-space: nowrap;
  }
  .person-role {
    color: var(--gold);
    font-size: 12px;
    margin-top: 2px;
  }
  .contact-list { list-style: none; margin-top: 22px; }
  .contact-list li {
    display: flex;
    justify-content: flex-end;
    align-items: center;
    gap: 8px;
    font-size: 12px;
    margin-bottom: 7px;
    white-space: nowrap;
  }
  .icon {
    width: 15px; height: 15px; flex: none;
    background: var(--gold);
    display: inline-flex; align-items: center; justify-content: center;
  }
  .icon svg { width: 10px; height: 10px; }
  .contact-list .email { font-size: 11px; margin-top: 30px; }

  /* Back */
  .card-back {
    left: 630px;
    background: linear-gradient(135deg, var(--navy) 0%, var(--navy-deep) 100%);
    color: var(--white);
  }
  .back-brand {
    position: absolute;
    left: 0; right: 0; top: 70px;
    text-align: center;
  }
  .back-brand .brand-mark {
    justify-content: center;
    font-size: 92px;
  }
  .back-brand .company-name { font-size: 22px; margin-top: 12px; }
  .address-band {
    position: absolute;
    left: 0; right: 0; bottom: 0;
    height: 46px;
    background: var(--white);
    border-top: 6px solid var(--navy);
  }
  .address {
    position: absolute;
    left: 0; right: 0; bottom: 52px;
    text-align: center;
    font-size: 14px;
  }
</style>
</head>
<body>
  <section class="card card-front">
    <svg class="shape" viewBox="0 0 520 318" preserveAspectRatio="none" aria-hidden="true">
      <path d="M230 0 C290 110 290 220 255 318 L520 318 L520 0 Z" fill="#1f3a82"/>
      <path d="M216 0 C276 110 276 220 241 318" fill="none" stroke="#f0a21e" stroke-width="4"/>
    </svg>
    <div class="front-brand">
      <div class="brand-mark"><span>TK</span><span class="brand-dot"></span></div>
      <p class="company-name">TK &amp; Co Finance Pty Ltd</p>
      <p class="licence">Licence No.: 718249</p>
    </div>
    <div class="contact">
      <p class="person-name">Desmond Okafor</p>
      <p class="person-role">Managing Director</p>
      <ul class="contact-list">
        <li>0417 638 294
          <span class="icon"><svg viewBox="0 0 10 10"><rect x="3" y="1" width="4" height="8" rx="1" fill="#fff"/></svg></span>
        </li>
        <li>03 9561 4472
          <span class="icon"><svg viewBox="0 0 10 10"><rect x="1" y="4" width="8" height="5" fill="#fff"/><rect x="3" y="1" width="4" height="3" fill="#fff"/></svg></span>
        </li>
        <li class="email">desmond.okafor@tkcolending.example
          <span class="icon"><svg viewBox="0 0 10 10"><rect x="1" y="2" width="8" height="6" fill="#fff"/><path d="M1 2 L5 6 L9 2" fill="none" stroke="#f0a21e" stroke-width="1"/></svg></span>
        </li>
      </ul>
    </div>
  </section>

  <section class="card card-back">
    <div class="back-brand">
      <div class="brand-mark"><span>TK</span><span class="brand-dot"></span></div>
      <p class="company-name">TK &amp; Co Finance Pty Ltd</p>
    </div>
    <p class="address">Suite 5/418 Marlow Avenue Elmvale Vic 3174</p>
    <div class="address-band"></div>
  </section>
</body>
</html>
```